Website Design for a New Business Sharing Application

Purpose: Website for a new product – a sharing application called "Gathr.io"

Product concept: Easy sharing of business information. The application has different sections: tasks, calendars, documents, contacts, notes and links. The key feature of the application is that you can drag and drop information from different sections into a "share." A share is a page which lists all the types of information that you drag into it. You can add people to this "share."

Note: The application itself is not part of this project, just the website.

Website details: The site, in addition to being informational, will actually be the first point of entry for visitors into the application itself. Because of that, we would like the website design to reflect the look of the application, to create a smooth and seamless experience for the user moving from the website into the application (tough the website does not need to look *exactly* like the application). Included Product Tour screenshots show you the look of the application.

Website pages to be created: 4 pages
We are flexible in terms of the exact structure and placement of elements. You may change that any way you like. The pages are as follows:

Home page
Product Tour page
Press page
Blog page

Specific description of pages are provided in project files we will upload. We will also upload the logo, home page layout we have in mind, and other supporting files.

NOTE: Please submit first the design of the home page. Based on this design we will ask selected designers to submit designs for the other pages.

Target Market(s)

Business people who want to share work related files with their colleagues

Industry/Entity Type

Business

Requirements
Must have
• All the required features are listed in the description of the website and specific pages that we will upload.

```html
<!DOCTYPE html>
<html lang="en">
<head>
<meta charset="utf-8">
<title>Gathr.io – Drag Files. Add People. Boom.</title>
<link href="https://fonts.googleapis.com/css2?family=Arimo:wght@400;700&family=PT+Sans:wght@400;700&family=Lobster&display=swap" rel="stylesheet">
<style>
  :root {
    --bar-dark: #262626;
    --bar-text: #b9b9b9;
    --hero-top: #f3c8a2;
    --hero-mid: #f7b97a;
    --hero-bottom: #f29a32;
    --ink: #2f271f;
    --panel-bg: #ebebeb;
    --panel-line: #cfcfcf;
    --page-bg: #f4f4f4;
    --body-text: #555555;
    --heading-text: #4a4a4a;
    --video-yellow: #e8a317;
    --player-dark: #222222;
    --button-blue: #6aaee0;
    --button-blue-dark: #4c92cc;
    --icon-grey: #8a8a8a;
  }
  * { box-sizing: border-box; margin: 0; padding: 0; }
  html, body { width: 1200px; height: 675px; overflow: hidden; }
  body { position: relative; background: var(--page-bg); font-family: "Arimo", Arial, sans-serif; }

  .top-bar { position: absolute; left: 0; top: 0; width: 1200px; height: 43px; background: var(--bar-dark); box-shadow: 0 1px 3px rgba(0,0,0,.4); z-index: 3; }
  .brand { position: absolute; left: 187px; top: 10px; display: flex; align-items: center; gap: 6px; font-family: "Arimo", sans-serif; font-weight: 700; font-size: 16px; color: #3d8fd1; }
  .brand-dot { width: 12px; height: 12px; border-radius: 50%; background: #e8761e; }
  .follow { position: absolute; left: 610px; top: 14px; display: flex; align-items: center; font-size: 12.5px; color: var(--bar-text); }
  .social { display: flex; gap: 7px; margin-left: 20px; }
  .social span { width: 17px; height: 17px; background: var(--icon-grey); border-radius: 2px; }
  .access { position: absolute; left: 904px; top: 16px; font-size: 11.5px; color: var(--bar-text); }
  .access::after { content: ""; display: inline-block; margin-left: 6px; border-left: 4px solid var(--bar-text); border-top: 3.5px solid transparent; border-bottom: 3.5px solid transparent; }

  .hero { position: absolute; left: 0; top: 43px; width: 1200px; height: 398px; background: linear-gradient(180deg, var(--hero-top) 0%, var(--hero-mid) 55%, var(--hero-bottom) 100%); }
  .headline { position: absolute; left: 185px; top: 32px; font-weight: 700; font-size: 51px; line-height: 53px; color: var(--ink); letter-spacing: -0.5px; }
  .headline .boom { background: linear-gradient(90deg, #1f4a2a, #7a1c1c 40%, #4a1830 70%, #2a2320); -webkit-background-clip: text; background-clip: text; color: transparent; }
  .pitch { position: absolute; left: 187px; top: 203px; width: 268px; font-family: "PT Sans", sans-serif; font-size: 15px; line-height: 22px; color: var(--ink); }

  .drop-zone { position: absolute; left: 538px; top: 27px; width: 476px; height: 176px; border: 2px dashed rgba(255,255,255,.9); border-radius: 4px; background: radial-gradient(ellipse at 50% 45%, #cdb1a6 0%, #c7b296 60%, #b9a98e 100%); box-shadow: inset 0 0 18px rgba(0,0,0,.25); display: flex; align-items: center; justify-content: center; font-weight: 700; font-size: 16px; color: #5a4a40; text-shadow: 0 1px 0 rgba(255,255,255,.5); }
  .or-divider { position: absolute; left: 538px; top: 212px; width: 476px; height: 40px; display: flex; align-items: center; gap: 14px; }
  .or-divider::before, .or-divider::after { content: ""; flex: 1; height: 2px; background: linear-gradient(90deg, transparent, rgba(90,60,30,.55), transparent); }
  .or-divider span { font-family: "Lobster", cursive; font-size: 32px; color: #5a4a40; }
  .email-input { position: absolute; left: 539px; top: 262px; width: 262px; height: 47px; background: #ececec; border: 1px solid #b9a48a; border-radius: 2px; padding-left: 11px; font-size: 16px; line-height: 45px; color: #8a8a8a; }
  .start-button { position: absolute; left: 818px; top: 262px; width: 195px; height: 47px; background: linear-gradient(180deg, var(--button-blue), var(--button-blue-dark)); border: 1px solid #4a88be; border-radius: 2px; text-align: center; line-height: 45px; font-size: 16px; color: #53728d; }

  .panel-back { position: absolute; left: 171px; top: 365px; width: 862px; height: 263px; background: var(--panel-bg); border-radius: 6px 6px 0 0; box-shadow: 0 -3px 6px rgba(160,60,10,.45); }
  .info-panel { position: absolute; left: 186px; top: 372px; width: 828px; height: 228px; background: var(--panel-bg); border: 1px solid var(--panel-line); }
  .info-panel h2 { position: absolute; top: 24px; font-size: 15.5px; font-weight: 700; color: var(--heading-text); }
  .what-title { left: 13px; }
  .how-title { left: 440px; }
  .what-text { position: absolute; left: 13px; top: 50px; width: 375px; font-size: 11px; line-height: 15.8px; color: var(--body-text); }
  .video { position: absolute; left: 452px; top: 61px; width: 350px; height: 147px; }
  .video-poster { width: 350px; height: 121px; background: var(--video-yellow); }
  .player-bar { height: 26px; background: var(--player-dark); display: flex; align-items: center; padding: 0 8px; gap: 12px; }
  .play { width: 0; height: 0; border-left: 11px solid #eee; border-top: 6px solid transparent; border-bottom: 6px solid transparent; }
  .progress { flex: 1; height: 6px; background: #ddd; border-radius: 3px; }

  .footer { position: absolute; left: 0; top: 620px; width: 1200px; height: 55px; }
  .footer svg { position: absolute; left: 0; top: 0; }
  .footer-nav { position: absolute; left: 0; top: 26px; width: 1200px; display: flex; justify-content: center; gap: 19px; font-size: 12.5px; color: var(--bar-text); padding-right: 4px; }
</style>
</head>
<body>
  <header class="top-bar">
    <div class="brand"><span class="brand-dot"></span>Gathr.io</div>
    <div class="follow">Follow Us On:
      <div class="social"><span></span><span></span><span></span></div>
    </div>
    <div class="access">Access Your Files</div>
  </header>

  <section class="hero">
    <h1 class="headline">Drag Files.<br>Add People.<br><span class="boom">Boom.</span></h1>
    <p class="pitch">Sharing with friends is simple, fast &amp; fun. Gathr.io brings the same ease to sharing with a partner, a contact at another company, a freelancer, a team-member OR a friend.</p>
    <div class="drop-zone">Drag Files Here</div>
    <div class="or-divider"><span>Or</span></div>
    <div class="email-input">Enter Business Email</div>
    <div class="start-button">Start Sharing</div>
  </section>

  <div class="panel-back"></div>
  <section class="info-panel">
    <h2 class="what-title">What Is It?</h2>
    <p class="what-text">This is Layerworks' version of Lorem Ipsum. Proin gravida nibh vel velit auctor aliquet. Aenean sollicitudin, lorem quis bibendum auctor, nisi elit consequat ipsum, nec sagittis sem nibh id elit. Duis sed odio sit amet nibh vulputate cursus a sit amet mauris. Morbi accumsan ipsum velit. Nam nec tellus a odio tincidunt auctor a ornare odio. Sed non mauris vitae erat consequat auctor eu in elit. Class aptent taciti sociosqu ad litora torquent per conubia nostra, per inceptos himenaeos. Mauris in erat justo. Nullam ac urna eu felis dapibus condimentum sit amet a augue. Sed non neque elit. Sed ut imperdiet nisi. Proin condimentum</p>
    <h2 class="how-title">See how it works</h2>
    <div class="video">
      <div class="video-poster" role="img" aria-label="Film reel illustration for the product video"></div>
      <div class="player-bar">
        <span class="play"></span>
        <span class="progress"></span>
        <svg width="16" height="14" viewBox="0 0 16 14"><path d="M1 5h3l4-3v10l-4-3H1z" fill="#eee"/><path d="M11 4q2 3 0 6M13 2q4 5 0 10" stroke="#eee" stroke-width="1.4" fill="none"/></svg>
      </div>
    </div>
  </section>

  <footer class="footer">
    <svg width="1200" height="55" viewBox="0 0 1200 55"><path d="M0 12 Q600 -6 1200 12 V55 H0 Z" fill="#262626"/></svg>
    <nav class="footer-nav">
      <span>Home</span><span>About Us</span><span>Product Tour</span><span>Pricing</span><span>Terms Of Use</span><span>Jobs</span><span>Sign Up</span><span>Blog</span><span>Press</span><span>Contact Us</span>
    </nav>
  </footer>
</body>
</html>
```